Concrete Construction Business Card design

We are a commercial concrete construction company based in Texas. a family owned business which our trade was passed down and taught by our grandfather whom we want represented in this design. our grandfathers nick name was "paprika" so we are wanting the letter G to be symbolized in some way with a red paprika . colors should be possibly a grey color back ground , green letter g and red paprika pepper , to be left for you to decide with integrity , concrete professionalism,and mexican heritage

Target Market(s)

general contractors, architects,inverstors, and engineers

Industry/Entity Type

Concrete

Contact Information for Business Card

Varela Concrete Construction LLC, Dwight Varela, 1718 Briarcliff Dr. Denton, TX 76209, (940)412-3759, dvslabworks58@mailbrook.net

```html
<!DOCTYPE html>
<html lang="en">
<head>
<meta charset="utf-8">
<title>Varela Concrete Construction LLC – Business Card</title>
<link rel="stylesheet" href="https://fonts.googleapis.com/css2?family=Andika:wght@400;700&display=swap">
<style>
  :root {
    --card-grey: #879891;
    --ink-dark: #1d3a30;
    --ink-white: #ffffff;
    --brand-green: #4ee81c;
    --plate-green-light: #9cff2a;
    --plate-green-deep: #4fcf00;
    --frame-silver-light: #f4f6f5;
    --frame-silver-dark: #9aa3a0;
    --shadow-dark: rgba(20, 30, 26, 0.75);
  }
  html, body {
    margin: 0;
    padding: 0;
    overflow: hidden;
    background: var(--card-grey);
  }
  .card {
    position: relative;
    width: 1200px;
    height: 702px;
    background: var(--card-grey);
    overflow: hidden;
    font-family: "Andika", sans-serif;
  }
  .brand-mark {
    position: absolute;
    left: 60px;
    top: 82px;
    width: 280px;
    display: flex;
    flex-direction: column;
    align-items: center;
    gap: 6px;
  }
  .brand-mark__square {
    width: 168px;
    height: 168px;
    background: var(--brand-green);
  }
  .brand-mark__name {
    font-family: "Andika", sans-serif;
    font-weight: 700;
    font-size: 64px;
    line-height: 80px;
    color: var(--brand-green);
    letter-spacing: 1px;
  }
  .company-name {
    position: absolute;
    left: 348px;
    top: 116px;
    margin: 0;
    font-weight: 700;
    font-size: 36px;
    letter-spacing: 2.8px;
    text-transform: uppercase;
    color: var(--ink-white);
    text-shadow: 2px 2px 2px var(--shadow-dark);
    white-space: nowrap;
  }
  .contact {
    position: absolute;
    left: 40px;
    top: 512px;
    width: 610px;
    text-align: center;
    color: var(--ink-dark);
    font-weight: 700;
    text-shadow:
      -2px -2px 0 var(--ink-white), 2px -2px 0 var(--ink-white),
      -2px 2px 0 var(--ink-white), 2px 2px 0 var(--ink-white),
      0 -2px 0 var(--ink-white), 0 2px 0 var(--ink-white),
      -2px 0 0 var(--ink-white), 2px 0 0 var(--ink-white);
    white-space: nowrap;
  }
  .contact__person {
    margin: 0;
    font-size: 44px;
    line-height: 58px;
    letter-spacing: 3.5px;
    text-transform: uppercase;
    padding-left: 74px;
  }
  .contact__phone {
    margin: 0;
    font-size: 36px;
    line-height: 56px;
    letter-spacing: 3.5px;
    padding-left: 30px;
  }
  .contact__email {
    margin: 0;
    font-size: 31px;
    line-height: 56px;
    letter-spacing: 1.8px;
  }
  .address-plate {
    position: absolute;
    left: 653px;
    top: 520px;
    width: 560px;
    height: 179px;
    border-radius: 12px;
    background: linear-gradient(180deg, var(--frame-silver-light), var(--frame-silver-dark) 55%, var(--frame-silver-light));
    box-sizing: border-box;
    padding: 12px 0 12px 14px;
    font-style: normal;
  }
  .address-plate__field {
    height: 100%;
    border-radius: 6px 0 0 6px;
    background: linear-gradient(180deg, var(--plate-green-light), var(--plate-green-deep));
    box-shadow: inset 0 0 8px rgba(0, 0, 0, 0.35);
    padding-top: 36px;
    padding-left: 20px;
    box-sizing: border-box;
  }
  .address-plate__line {
    margin: 0;
    font-weight: 700;
    font-size: 43px;
    line-height: 44px;
    letter-spacing: 4px;
    color: var(--ink-white);
    text-shadow: 2px 2px 2px var(--shadow-dark);
    white-space: nowrap;
  }
  .address-plate__line--second {
    padding-left: 48px;
  }
</style>
</head>
<body>
  <main class="card">
    <div class="brand-mark">
      <span class="brand-mark__square"></span>
      <span class="brand-mark__name">Varela</span>
    </div>

    <h1 class="company-name">Varela Concrete Construction LLC</h1>

    <section class="contact">
      <p class="contact__person">Dwight Varela</p>
      <p class="contact__phone">(940)412-3759</p>
      <p class="contact__email">dvslabworks58@mailbrook.net</p>
    </section>

    <address class="address-plate">
      <div class="address-plate__field">
        <p class="address-plate__line">1718 Briarcliff Dr.</p>
        <p class="address-plate__line address-plate__line--second">Denton, TX 76209</p>
      </div>
    </address>
  </main>
</body>
</html>
```